Bastion Electronic Security Web Site

We need a web site for our new company based in Sydney Australia.
We specialize in consulting supplying and installing electronic security systems. These include CCTV, Access control, Alarms, Intercom and Network cabling.
We pride our selves in giving our customers peace of mind giving back security and freedom to our customers. We pride in customer service quality products and expertise with and we do the job as though it is for our personal friends and family.
We need to be able to edit web site contents and update information.
Industry/Entity Type
Electronic

```html
<!DOCTYPE html>
<html lang="en">
<head>
<meta charset="utf-8">
<title>Bastion Electronic Security</title>
<link href="https://fonts.googleapis.com/css2?family=Cabin:wght@400;500;600&display=swap" rel="stylesheet">
<style>
:root{
  --orange:#f39a2c;
  --orange-dark:#e8811a;
  --orange-light:#f7ad4a;
  --text:#555;
  --heading:#222;
  --white:#fff;
  --line:#d8d8d8;
}
*{box-sizing:border-box;margin:0;padding:0}
html,body{width:766px;height:1200px;overflow:hidden}
body{font-family:'Cabin',sans-serif;background:var(--white);position:relative;color:var(--text)}
.abs{position:absolute}
.header{left:0;top:0;width:766px;height:73px;background:linear-gradient(#2c2c2c,#141414)}
.brand{left:94px;top:29px;font-size:15.5px;color:var(--orange);font-weight:500;text-transform:uppercase}
.social{left:589px;top:30px;display:flex;gap:7px}
.social span{width:14px;height:14px;background:var(--orange);display:block;border-radius:2px}
.nav{left:0;top:73px;width:766px;height:44px;background:linear-gradient(var(--orange-light),var(--orange-dark));display:flex;align-items:center;padding-left:90px;gap:14.5px}
.nav a{color:var(--white);font-size:11px;text-decoration:none;text-transform:uppercase}
.hero{left:0;top:117px;width:766px;height:291px;background:linear-gradient(90deg,#eef1f6 0%,#f5f6f9 45%,#c9ccd0 75%,#8f9296 100%)}
.hero-caption{left:94px;top:256px;width:397px;height:75px;background:rgba(243,154,44,.92);color:var(--white);font-size:15.5px;line-height:23px;padding:14px 20px;text-transform:uppercase}
.arrow{top:257px}
.welcome{top:422px;left:0;width:766px;text-align:center}
h2{color:var(--orange);font-size:16px;font-weight:400;text-transform:uppercase}
.intro{width:545px;margin:5px auto 0;font-size:8.4px;line-height:11.6px;color:var(--text)}
.btn{display:inline-block;background:var(--orange);color:var(--white);font-size:8.5px;border-radius:3px;text-align:center}
.learn{margin-top:5px;width:76px;height:24px;line-height:24px;text-transform:uppercase}
.services-head{top:533px;left:0;width:766px;text-align:center}
.services-head p{font-size:9px;color:#444;margin-top:3px}
.card{top:581px;width:147px;height:190px;border:1px solid var(--line);background:var(--white)}
.card .photo{height:110px}
.card h3{font-size:9px;font-weight:400;color:var(--heading);margin:10px 9px 3px}
.card p{font-size:8.6px;line-height:10px;margin:0 9px;color:var(--text)}
.next{left:642px;top:781px;font-size:10px;color:#333;display:flex;align-items:center;gap:4px}
.newsletter{top:836px;left:99px;width:580px;height:27px;font-size:10px;color:var(--heading)}
.newsletter .field{font-size:8px;color:#666}
.submit{width:85px;height:26px;line-height:26px;font-size:10px}
.map{left:0;top:883px;width:766px;height:239px;background:linear-gradient(120deg,#f9e6c8,#f6dfbb 60%,#f9e7cb)}
.cf-title{left:82px;top:893px;font-size:16px;color:var(--heading)}
.label{left:92px;font-size:8.5px;color:#333}
.input{left:130px;width:258px;background:var(--white)}
.cbox{left:438px;top:898px;width:156px;height:162px;background:var(--white)}
.cbox .top{height:30px;background:linear-gradient(var(--orange-light),var(--orange-dark));color:var(--white);font-size:11px;padding:8px 23px}
.cbox .lines{font-size:8.5px;line-height:15.4px;color:#333;padding:14px 0 0 50px;position:relative}
.footer{left:0;top:1122px;width:766px;height:78px;background:linear-gradient(#2a2a2a,#151515)}
.fnav{left:80px;top:1140px;display:flex;gap:15px}
.fnav a{color:var(--white);font-size:8.3px;text-decoration:none;text-transform:uppercase}
.fsocial{left:559px;top:1131px;display:flex;gap:6px}
.fsocial span{width:20px;height:20px;border-radius:50%;background:#d9d9d9;display:block}
.copy{left:551px;top:1171px;font-size:8px;color:var(--white)}
</style>
</head>
<body>
<header class="abs header">
  <div class="abs brand">Bastion Electronic Security</div>
  <div class="abs social"><span></span><span></span><span></span><span></span></div>
</header>
<nav class="abs nav">
  <a>Home</a><a>About Us</a><a>Services</a><a>Products</a><a>News</a><a>Testimonials</a><a>Gallery</a><a>Contact Us</a>
</nav>
<section class="abs hero" role="img" aria-label="Close-up photo of a security camera lens on a bright background"></section>
<svg class="abs arrow" style="left:19px" width="33" height="33" viewBox="0 0 33 33"><circle cx="16.5" cy="16.5" r="15" fill="none" stroke="#888" stroke-width="2"/><path d="M20 10 L11 16.5 L20 23 Z" fill="none" stroke="#888" stroke-width="2"/></svg>
<svg class="abs arrow" style="left:710px" width="33" height="33" viewBox="0 0 33 33"><circle cx="16.5" cy="16.5" r="15" fill="none" stroke="#666" stroke-width="2"/><path d="M13 10 L22 16.5 L13 23 Z" fill="none" stroke="#666" stroke-width="2"/></svg>
<div class="abs hero-caption">We specialize in consulting supplying and installing electronic security systems</div>

<section class="abs welcome">
  <h2>Welcome to our website</h2>
  <p class="intro">Duis aute irure dolor in reprehenderit in voluptate velit esse cillum dolore eu fugiat nulla pariatur. Excepteur sint occaecat cupidatat non proident, sunt in culpa qui officia deserunt mollit anim id est laborum Neque porro quisquam est, qui dolorem ipsum quia dolor sit amet, consectetur, adipisci velit, sed quia non numquam eius modi tempora incidunt ut labore et dolore magnam aliquam quaerat voluptatem. Ut enim ad minima veniam, quis nostrum exercitationem ullam corporis suscipit</p>
  <span class="btn learn">Learn More</span>
</section>

<section class="abs services-head">
  <h2>Our Services</h2>
  <p>We do services in house break-in by</p>
</section>

<article class="abs card" style="left:80px"><div class="photo" role="img" aria-label="Black and white photo of a CCTV camera" style="background:linear-gradient(135deg,#e8e8e8,#777)"></div><h3>CCTV</h3><p>Duis aute irure dolor in reprehenderit in voluptate velit esse cillum dolore eu fugiat nulla pariatur.</p></article>
<article class="abs card" style="left:233px"><div class="photo" role="img" aria-label="Photo of a person using an access control keypad" style="background:linear-gradient(135deg,#cfd8e2,#8d949c)"></div><h3>Access control</h3><p>Duis aute irure dolor in reprehenderit in voluptate velit esse cillum dolore eu fugiat nulla pariatur.</p></article>
<article class="abs card" style="left:387px"><div class="photo" role="img" aria-label="Photo of a smoke alarm with smoke" style="background:linear-gradient(135deg,#e4e2dd,#a9aeb6)"></div><h3>Alarms</h3><p>Duis aute irure dolor in reprehenderit in voluptate velit esse cillum dolore eu fugiat nulla pariatur.</p></article>
<article class="abs card" style="left:540px"><div class="photo" role="img" aria-label="Photo of a hand pressing an intercom panel" style="background:linear-gradient(135deg,#d9dcd6,#efeeea 60%,#7a7a72)"></div><h3>Intercom and Network cabling</h3><p>Duis aute irure dolor in reprehenderit in voluptate velit esse cillum dolore eu fugiat nulla pariatur.</p></article>

<div class="abs next">NEXT <svg width="10" height="18" viewBox="0 0 10 18"><path d="M2 1 L9 9 L2 17" fill="none" stroke="#333" stroke-width="1.3"/></svg></div>

<div class="abs newsletter">
  <svg class="abs" style="left:0;top:7px" width="16" height="12" viewBox="0 0 16 12"><rect x="1" y="1" width="14" height="10" fill="none" stroke="#222" stroke-width="1.5"/><path d="M1 1 L8 7 L15 1" fill="none" stroke="#222" stroke-width="1.5"/></svg>
  <span class="abs" style="left:28px;top:6px">Subscribe Newsletter</span>
  <span class="abs field" style="left:144px;top:10px">Name</span>
  <span class="abs field" style="left:324px;top:10px">Email</span>
  <span class="abs btn submit" style="left:495px;top:0">Submit</span>
</div>

<section class="abs map" role="img" aria-label="Street map of the surrounding area"></section>
<div class="abs cf-title">Contact Form</div>
<span class="abs label" style="top:935px">Name</span>
<span class="abs label" style="top:974px">Email</span>
<span class="abs label" style="top:1012px">Message</span>
<div class="abs input" style="top:923px;height:33px"></div>
<div class="abs input" style="top:961px;height:32px"></div>
<div class="abs input" style="top:997px;height:61px"></div>
<span class="abs btn submit" style="left:308px;top:1071px;width:76px;height:27px;line-height:27px;border-radius:0">SUBMIT</span>

<aside class="abs cbox">
  <div class="top">Contact Us</div>
  <div class="lines">
    <svg class="abs" style="left:37px;top:18px" width="8" height="8" viewBox="0 0 8 8"><path d="M0 4 L4 0 L8 4 L7 4 L7 8 L1 8 L1 4 Z" fill="#555"/></svg>
    Harbour Works<br>Unit 7 Lantern Row<br>Examplevale NSW<br><br>
    <svg class="abs" style="left:37px;top:78px" width="8" height="8" viewBox="0 0 8 8"><path d="M1 0 L3 0 L3.5 2 L2.5 3 Q3.5 5 5 5.5 L6 4.5 L8 5 L8 7 Q4 8 1 4 Q0 2 1 0Z" fill="#555"/></svg>
    Tel: +61 2 5550 4120<br>
    <svg class="abs" style="left:37px;top:94px" width="7" height="8" viewBox="0 0 7 8"><path d="M0 0 H5 L7 2 V8 H0Z" fill="#555"/></svg>
    Fax: +61 2 5550 4121
  </div>
</aside>

<footer class="abs footer"></footer>
<nav class="abs fnav"><a>Home</a><a>About Us</a><a>Services</a><a>Products</a><a>News</a><a>Testimonials</a><a>Gallery</a><a>Contact Us</a></nav>
<div class="abs fsocial"><span></span><span></span><span></span><span></span><span></span></div>
<div class="abs copy">©2014.www.bastionsecure.example</div>
</body>
</html>
```